Powerpoint master slides for business

Hello everyone,

I am looking for a new PowerPoint master slide that should be modern, slim and yet suitable for business.

I have uploaded a few pictures, which should serve as A. orientation for my presentation. A logo should be placed on the right-hand side of the cover sheet and all subsequent slides - please insert a placeholder here. Also attached are our company colors, which must be taken into account.

Basically, I would find 6 to 10 slides (cover sheet, classic slide, end, etc.) good.

PS: The slides are intended for general everyday work, ie the design should be subtle and easily adaptable to different situations, but still look chic, modern and classy.

```html
<!DOCTYPE html>
<html lang="en">
<head>
<meta charset="utf-8">
<title>Verdano – Business Master Slides</title>
<link href="https://fonts.googleapis.com/css2?family=Montserrat:wght@400;500;600;700;800&display=swap" rel="stylesheet">
<style>
:root{
  --navy:#1a1a4f;
  --green:#6dbf47;
  --green-dark:#4f9a32;
  --grey-bg:#d7d7d7;
  --grey-bar:#9a9a9e;
  --ink:#2a2a33;
  --white:#ffffff;
}
*{margin:0;padding:0;box-sizing:border-box}
html,body{width:772px;height:1200px;overflow:hidden}
body{background:var(--grey-bg);font-family:'Montserrat',sans-serif;color:var(--ink);position:relative}
.slide{position:absolute;width:287px;height:180px;background:var(--white);overflow:hidden;box-shadow:0 6px 6px -4px rgba(0,0,0,.35)}
.abs{position:absolute}
.logo{position:absolute;display:flex;align-items:center;gap:2px;font-weight:600;color:var(--navy);white-space:nowrap}
.logo .dot{border-radius:50%;background:var(--navy);display:inline-block}
.logo.small{font-size:6.5px;top:8px;right:11px}
.logo.small .dot{width:6px;height:6px}
.logo.large{font-size:15px;right:10px}
.logo.large .dot{width:13px;height:13px;margin-right:2px}
.logo.light{color:var(--white)}
.logo.light .dot{background:var(--white)}
.top-bar{position:absolute;left:0;top:9px;width:245px;height:5px;background:var(--green);border-radius:0 3px 3px 0}
.foot-bar{position:absolute;left:0;bottom:0;width:100%;height:6px;background:var(--navy)}
.page-pill{position:absolute;right:10px;bottom:3.5px;height:6px;padding:0 4px;border-radius:3px;background:var(--green);color:var(--white);font-size:2.8px;font-weight:700;line-height:6px}
.tiny{font-size:3.5px;line-height:4.6px;color:var(--ink)}
.just{text-align:justify}
.center{text-align:center}
.slide-title{font-size:9px;font-weight:500;color:var(--navy);white-space:nowrap}
.slide-title b{color:var(--green);font-weight:600}
.slide-title.title-green{color:var(--green);font-weight:600}
.rule{position:absolute;height:1px;background:var(--green)}
.photo{position:absolute}
.icon-badge{position:absolute;border-radius:50%;display:flex;align-items:center;justify-content:center}
.icon-badge svg{width:55%;height:55%}
.svc-title{font-size:7px;color:var(--navy);white-space:nowrap}
.svc-sub{font-size:3.6px;color:var(--ink);white-space:nowrap}
.col-head{font-size:7px;color:var(--green);font-weight:500;text-align:center}
.box{position:absolute;width:54.5px;height:81.5px;color:var(--white);text-align:center}
.box .tiny{color:var(--white);padding:0 4px}
.box h4{font-size:7px;font-weight:400;margin-top:4px}
.box .icon-badge{position:relative;margin:6px auto 0;width:10px;height:10px}
.fill-navy{background:var(--navy)}
.fill-green{background:var(--green)}
</style>
</head>
<body>

<svg width="0" height="0" style="position:absolute">
  <symbol id="person" viewBox="0 0 20 20">
    <circle cx="10" cy="6" r="4" fill="currentColor"/>
    <path d="M2 19c0-5 3.5-8 8-8s8 3 8 8z" fill="currentColor"/>
  </symbol>
</svg>

<!-- Cover -->
<section class="slide" style="left:79px;top:78px">
  <div class="logo large" style="top:13px"><span class="dot"></span>Verdano</div>
  <svg class="photo" style="left:0;top:42px" width="287" height="115" viewBox="0 0 287 115">
    <defs>
      <linearGradient id="meet" x1="0" y1="0" x2="1" y2="1">
        <stop offset="0" stop-color="#cfd7e6"/><stop offset=".6" stop-color="#6e7c9c"/><stop offset="1" stop-color="#2d3a66"/>
      </linearGradient>
    </defs>
    <rect width="287" height="115" fill="var(--navy)"/>
    <polygon points="0,0 171,0 107,115 0,115" fill="url(#meet)" role="img" aria-label="Photo of a business meeting around a conference table"/>
    <polygon points="171,0 180,0 116,115 107,115" fill="#2c2c66" opacity=".6"/>
  </svg>
  <div class="abs" style="right:10px;top:87px;text-align:right">
    <div style="font-size:12px;font-weight:700;color:var(--green);line-height:13px">PRESENTATION</div>
    <div style="font-size:12px;font-weight:600;color:var(--white);line-height:13px">TITLE GOES HERE</div>
    <div style="font-size:5px;color:var(--white);margin-top:4px">Subtitle of Presentation Goes Here</div>
    <div style="font-size:4.5px;color:var(--white);margin-top:15px">Friday, August, 2023</div>
  </div>
  <div class="abs center" style="left:0;width:100%;top:163px;font-size:4.5px;color:#777">© Copyright Verdano All Right Reserved</div>
</section>

<!-- Services list -->
<section class="slide" style="left:406px;top:78px">
  <div class="top-bar"></div>
  <div class="logo small"><span class="dot"></span>Verdano</div>
  <svg class="photo" style="left:0;top:42px" width="180" height="115" viewBox="0 0 180 115">
    <defs><linearGradient id="gphoto" x1="0" y1="0" x2="1" y2="1"><stop offset="0" stop-color="#8bd160"/><stop offset="1" stop-color="#4e9a2f"/></linearGradient></defs>
    <polygon points="0,0 131,0 178,115 0,115" fill="url(#gphoto)" role="img" aria-label="Green-toned photo of colleagues talking in an office"/>
  </svg>
  <div class="icon-badge fill-navy" style="left:132px;top:53px;width:15px;height:15px;color:#fff"><svg><use href="#person"/></svg></div>
  <div class="abs" style="left:156px;top:53px"><div class="svc-title">Service Title Goes Here</div><div class="svc-sub">Vivamus eu dull ex. curobour dopibus</div></div>
  <div class="icon-badge fill-navy" style="left:142px;top:79px;width:15px;height:15px;color:#fff"><svg><use href="#person"/></svg></div>
  <div class="abs" style="left:167px;top:79px"><div class="svc-title">Service Title Goes Here</div><div class="svc-sub">Vivamus eu dull ex. curobour dopibus</div></div>
  <div class="icon-badge fill-navy" style="left:152px;top:105px;width:15px;height:15px;color:#fff"><svg><use href="#person"/></svg></div>
  <div class="abs" style="left:177px;top:104px"><div class="svc-title">Service Title Goes Here</div><div class="svc-sub">Vivamus eu dull ex. curobour dopibus</div></div>
  <div class="icon-badge fill-navy" style="left:163px;top:131px;width:15px;height:15px;color:#fff"><svg><use href="#person"/></svg></div>
  <div class="abs" style="left:188px;top:130px"><div class="svc-title">Service Title Goes Here</div><div class="svc-sub">Vivamus eu dull ex. curobour dopibus</div></div>
  <div class="foot-bar"></div><div class="page-pill">PAGE - 01</div>
</section>

<!-- Our Service (five) -->
<section class="slide" style="left:79px;top:290px">
  <div class="photo" role="img" aria-label="Navy-tinted photo of a team in a meeting" style="left:0;top:0;width:287px;height:91.5px;background:linear-gradient(120deg,#2a2a62,#1a1a4f 60%,#23235a)"></div>
  <div class="logo small light" style="top:8px"><span class="dot"></span>Verdano</div>
  <div class="slide-title abs center" style="left:0;width:100%;top:8px;color:#fff">Our <b>Service</b></div>
  <p class="tiny center abs" style="left:50px;width:187px;top:28px;color:#fff;line-height:4.5px">Lorem ipsum dolor sit amet, consectetuer adipiscing elit, sed diam nonummy nibh euismod tincidunt ut laoreet dolore magna aliquam erat volutpat. Ut wisi enim ad minim veniam, quis nostrud exerci tation ullamcorper suscipit lobortis nisl ut aliquip ex ea commodo consequat. Duis autem vel eum iriure dolor in hendrerit in vulputate velit esse molestie consequat.</p>
  <svg class="abs" style="left:0;top:60px" width="287" height="30"><line x1="37" y1="14" x2="250" y2="14" stroke="var(--green)" stroke-width=".4" opacity=".6"/></svg>
  <div class="icon-badge" style="left:27px;top:63px;width:21px;height:21px;border:1px solid var(--green);color:#fff;background:var(--navy)"><svg><use href="#person"/></svg></div>
  <div class="icon-badge" style="left:80px;top:63px;width:21px;height:21px;border:1px solid var(--green);color:#fff;background:var(--navy)"><svg><use href="#person"/></svg></div>
  <div class="icon-badge" style="left:133px;top:63px;width:21px;height:21px;border:1px solid var(--green);color:#fff;background:var(--navy)"><svg><use href="#person"/></svg></div>
  <div class="icon-badge" style="left:186px;top:63px;width:21px;height:21px;border:1px solid var(--green);color:#fff;background:var(--navy)"><svg><use href="#person"/></svg></div>
  <div class="icon-badge" style="left:240px;top:63px;width:21px;height:21px;border:1px solid var(--green);color:#fff;background:var(--navy)"><svg><use href="#person"/></svg></div>
  <div class="abs center" style="left:12px;width:50px;top:95px"><div class="svc-title" style="font-size:6px;line-height:6.5px">Service Title<br>Goes Here</div><div class="tiny" style="margin-top:3px">Vivamus eu dull ex.<br>curobour dopibus</div></div>
  <div class="abs center" style="left:65px;width:50px;top:95px"><div class="svc-title" style="font-size:6px;line-height:6.5px">Service Title<br>Goes Here</div><div class="tiny" style="margin-top:3px">Vivamus eu dull ex.<br>curobour dopibus</div></div>
  <div class="abs center" style="left:118px;width:50px;top:95px"><div class="svc-title" style="font-size:6px;line-height:6.5px">Service Title<br>Goes Here</div><div class="tiny" style="margin-top:3px">Vivamus eu dull ex.<br>curobour dopibus</div></div>
  <div class="abs center" style="left:172px;width:50px;top:95px"><div class="svc-title" style="font-size:6px;line-height:6.5px">Service Title<br>Goes Here</div><div class="tiny" style="margin-top:3px">Vivamus eu dull ex.<br>curobour dopibus</div></div>
  <div class="abs center" style="left:225px;width:50px;top:95px"><div class="svc-title" style="font-size:6px;line-height:6.5px">Service Title<br>Goes Here</div><div class="tiny" style="margin-top:3px">Vivamus eu dull ex.<br>curobour dopibus</div></div>
  <div class="foot-bar"></div><div class="page-pill">PAGE - 01</div>
</section>

<!-- About Us -->
<section class="slide" style="left:406px;top:290px">
  <div class="top-bar"></div>
  <div class="logo small"><span class="dot"></span>Verdano</div>
  <div class="slide-title abs" style="left:10px;top:51px">About <b style="color:var(--navy)">Us</b></div>
  <div class="rule" style="left:10px;top:65px;width:45px"></div>
  <p class="tiny just abs" style="left:10px;top:77px;width:126px">Lorem ipsum dolor sit amet, consectetuer adipiscing elit, sed diam nonummy nibh euismod tincidunt ut laoreet dolore magna aliquam erat volutpat. Ut wisi enim ad minim veniam, quis nostrud exerci tation ullamcorper suscipit lobortis nisl ut aliquip ex ea commodo consequat. Duis autem vel eum iriure dolor in hendrerit in vulputate velit esse molestie consequat.</p>
  <p class="tiny just abs" style="left:10px;top:112px;width:126px">Lorem ipsum dolor sit amet, consectetuer adipiscing elit, sed diam nonummy nibh euismod tincidunt ut laoreet dolore magna aliquam erat volutpat. Ut wisi enim ad minim veniam, quis nostrud exerci tation ullamcorper suscipit lobortis nisl ut aliquip ex ea commodo consequat. Duis autem vel eum iriure dolor in hendrerit in vulputate velit esse molestie consequat.</p>
  <div class="abs" style="left:163px;top:49px;width:109px;height:104px;background:var(--green);border-radius:5px"></div>
  <div class="photo" role="img" aria-label="Photo of colleagues working at laptops in a bright office" style="left:156px;top:39px;width:112px;height:110px;border-radius:5px;background:linear-gradient(135deg,#eceef0,#a9abb0 55%,#4d4f55)"></div>
  <div class="foot-bar"></div><div class="page-pill">PAGE - 01</div>
</section>

<!-- Heading + three columns -->
<section class="slide" style="left:79px;top:502px">
  <div class="top-bar"></div>
  <div class="logo small"><span class="dot"></span>Verdano</div>
  <div class="photo" role="img" aria-label="Wide greyscale photo of women working at computers" style="left:11px;top:28px;width:266px;height:51px;background:linear-gradient(90deg,#5a5a5e,#c9c9cc 40%,#8a8a8f 70%,#dcdcde)"></div>
  <div class="abs" style="left:11px;top:86px;font-size:9px;line-height:10px"><div style="color:var(--green)">Heading</div><div style="color:var(--navy)">Goes Here</div></div>
  <div class="rule" style="left:11px;top:109px;width:42px"></div>
  <p class="tiny abs" style="left:11px;top:116px;width:76px">Lorem ipsum dolor sit amet, consectetuer adipiscing elit, sed diam nonummy nibh euismod tincidunt ut laoreet dolore magna aliquam erat volutpat. Ut wisi enim ad minim veniam, quis nostrud exerci tation</p>
  <div class="icon-badge fill-green" style="left:123px;top:74px;width:10px;height:10px;color:#fff;border:1px solid #fff"><svg><use href="#person"/></svg></div>
  <div class="icon-badge fill-green" style="left:183px;top:74px;width:10px;height:10px;color:#fff;border:1px solid #fff"><svg><use href="#person"/></svg></div>
  <div class="icon-badge fill-green" style="left:243px;top:74px;width:10px;height:10px;color:#fff;border:1px solid #fff"><svg><use href="#person"/></svg></div>
  <div class="abs" style="left:106px;width:45px;top:90px"><div class="col-head">Heading</div><p class="tiny center" style="margin-top:3px">Lorem ipsum dolor sit amet, consectetuer adipiscing elit, sed diam nonummy nibh euismod tincidunt ut laoreet dolore magna aliquam erat volutpat. Ut wisi enim ad minim veniam, quis nostrud exerci tation</p></div>
  <div class="abs" style="left:166px;width:45px;top:90px"><div class="col-head">Heading</div><p class="tiny center" style="margin-top:3px">Lorem ipsum dolor sit amet, consectetuer adipiscing elit, sed diam nonummy nibh euismod tincidunt ut laoreet dolore magna aliquam erat volutpat. Ut wisi enim ad minim veniam, quis nostrud exerci tation</p></div>
  <div class="abs" style="left:226px;width:45px;top:90px"><div class="col-head">Heading</div><p class="tiny center" style="margin-top:3px">Lorem ipsum dolor sit amet, consectetuer adipiscing elit, sed diam nonummy nibh euismod tincidunt ut laoreet dolore magna aliquam erat volutpat. Ut wisi enim ad minim veniam, quis nostrud exerci tation</p></div>
  <div class="foot-bar"></div><div class="page-pill">PAGE - 01</div>
</section>

<!-- Our Service with progress rings -->
<section class="slide" style="left:406px;top:502px">
  <div class="top-bar"></div>
  <div class="logo small"><span class="dot"></span>Verdano</div>
  <div class="slide-title abs" style="left:12px;top:24px">Our <b>Service</b></div>
  <div class="rule" style="left:12px;top:37px;width:56px"></div>
  <div class="icon-badge" style="left:12px;top:53px;width:15px;height:15px;border:.6px solid var(--green);color:var(--green)"><svg><use href="#person"/></svg></div>
  <div class="abs" style="left:33px;top:53px"><div class="svc-title" style="color:var(--green);font-size:6.5px">Service Title Goes Here</div><div class="svc-sub">Vivamus eu dull ex. curobour dopibus</div></div>
  <p class="tiny abs" style="left:12px;top:68px;width:264px">Lorem ipsum dolor sit amet, consectetuer adipiscing elit, sed diam nonummy nibh euismod tincidunt ut laoreet dolore magna aliquam erat volutpat. Ut wisi enim ad minim veniam, quis nostrud exerci tation ullamcorper suscipit lobortis nisl ut aliquip ex ea commodo consequat. Duis autem vel eum iriure dolor in hendrerit in vulputate velit esse molestie consequat.</p>
  <svg class="abs" style="left:0;top:98px" width="287" height="40" viewBox="0 0 287 40">
    <g fill="none" stroke-width="2.4">
      <circle cx="59" cy="19" r="15.5" stroke="var(--green)"/><circle cx="59" cy="19" r="15.5" stroke="var(--navy)" stroke-dasharray="24.3 97.4" transform="rotate(180 59 19)"/>
      <circle cx="115" cy="19" r="15.5" stroke="var(--green)"/><circle cx="115" cy="19" r="15.5" stroke="var(--navy)" stroke-dasharray="24.3 97.4" transform="rotate(180 115 19)"/>
      <circle cx="171" cy="19" r="15.5" stroke="var(--green)"/><circle cx="171" cy="19" r="15.5" stroke="var(--navy)" stroke-dasharray="24.3 97.4" transform="rotate(180 171 19)"/>
      <circle cx="227" cy="19" r="15.5" stroke="var(--green)"/><circle cx="227" cy="19" r="15.5" stroke="var(--navy)" stroke-dasharray="24.3 97.4" transform="rotate(180 227 19)"/>
    </g>
    <g fill="var(--green)" font-family="Montserrat, sans-serif" font-size="8" text-anchor="middle">
      <text x="59" y="22">75%</text><text x="115" y="22">75%</text><text x="171" y="22">75%</text><text x="227" y="22">75%</text>
    </g>
  </svg>
  <div class="abs center" style="left:34px;width:50px;top:138px"><div style="font-size:5px;font-weight:600;color:var(--navy)">Heading</div><div class="tiny" style="line-height:3.8px">adipiscing elit. Vivamus<br>eu dui ex. Cutabitur</div></div>
  <div class="abs center" style="left:90px;width:50px;top:138px"><div style="font-size:5px;font-weight:600;color:var(--navy)">Heading</div><div class="tiny" style="line-height:3.8px">adipiscing elit. Vivamus<br>eu dui ex. Cutabitur</div></div>
  <div class="abs center" style="left:146px;width:50px;top:138px"><div style="font-size:5px;font-weight:600;color:var(--navy)">Heading</div><div class="tiny" style="line-height:3.8px">adipiscing elit. Vivamus<br>eu dui ex. Cutabitur</div></div>
  <div class="abs center" style="left:202px;width:50px;top:138px"><div style="font-size:5px;font-weight:600;color:var(--navy)">Heading</div><div class="tiny" style="line-height:3.8px">adipiscing elit. Vivamus<br>eu dui ex. Cutabitur</div></div>
  <div class="foot-bar"></div><div class="page-pill">PAGE - 01</div>
</section>

<!-- Chart -->
<section class="slide" style="left:79px;top:714px">
  <div class="top-bar"></div>
  <div class="logo small"><span class="dot"></span>Verdano</div>
  <div class="slide-title title-green abs" style="left:12px;top:20px;font-size:8.5px">Heading <span style="font-weight:400">Goes Here</span></div>
  <p class="tiny abs" style="left:13px;top:51px;width:142px">Lorem ipsum dolor sit amet, consectetuer adipiscing elit, sed diam nonummy nibh euismod tincidunt ut laoreet dolore magna aliquam erat volutpat. Ut wisi enim ad minim veniam, quis nostrud exerci tation</p>
  <svg class="abs" style="left:10px;top:74px" width="156" height="70" viewBox="0 0 156 70" font-family="Montserrat, sans-serif">
    <g stroke="#d0d0d0" stroke-width=".3">
      <line x1="10" y1="4" x2="153" y2="4"/><line x1="10" y1="13.8" x2="153" y2="13.8"/><line x1="10" y1="23.7" x2="153" y2="23.7"/><line x1="10" y1="33.5" x2="153" y2="33.5"/><line x1="10" y1="43.3" x2="153" y2="43.3"/><line x1="10" y1="53.2" x2="153" y2="53.2"/><line x1="10" y1="63" x2="153" y2="63"/>
    </g>
    <g font-size="3" fill="#333" text-anchor="end">
      <text x="7" y="5">6</text><text x="7" y="14.8">5</text><text x="7" y="24.7">4</text><text x="7" y="34.5">3</text><text x="7" y="44.3">2</text><text x="7" y="54.2">1</text><text x="7" y="64">0</text>
    </g>
    <rect x="16" y="20.7" width="8" height="42.3" fill="var(--green)"/><rect x="25" y="39.4" width="8" height="23.6" fill="var(--grey-bar)"/><rect x="34" y="43.3" width="8" height="19.7" fill="var(--navy)"/>
    <rect x="52" y="38.4" width="8" height="24.6" fill="var(--grey-bar)"/><rect x="61" y="19.7" width="8" height="43.3" fill="var(--green)"/><rect x="70" y="43.3" width="8" height="19.7" fill="var(--navy)"/>
    <rect x="88" y="28.6" width="8" height="34.4" fill="var(--navy)"/><rect x="97" y="45.3" width="8" height="17.7" fill="var(--grey-bar)"/><rect x="106" y="33.5" width="8" height="29.5" fill="var(--green)"/>
    <rect x="124" y="18.7" width="8" height="44.3" fill="var(--grey-bar)"/><rect x="133" y="35.4" width="8" height="27.6" fill="var(--navy)"/><rect x="142" y="13.8" width="8" height="49.2" fill="var(--green)"/>
    <g font-size="3" fill="#333" text-anchor="middle">
      <text x="29" y="68">Category 1</text><text x="65" y="68">Category 2</text><text x="101" y="68">Category 3</text><text x="137" y="68">Category 4</text>
    </g>
  </svg>
  <div class="photo" role="img" aria-label="Photo of hands reviewing printed charts beside a laptop" style="left:178px;top:37px;width:97px;height:120px;background:linear-gradient(160deg,#1f2433,#6a6f7c 40%,#e6e8ec 70%,#8b6a4f)"></div>
  <div class="foot-bar"></div><div class="page-pill">PAGE - 01</div>
</section>

<!-- Four boxes -->
<section class="slide" style="left:406px;top:714px">
  <div class="top-bar"></div>
  <div class="logo small"><span class="dot"></span>Verdano</div>
  <div class="slide-title title-green abs" style="left:12px;top:20px;font-size:8.5px">Heading <span style="font-weight:400">Goes Here</span></div>
  <p class="tiny abs" style="left:11px;top:39px;width:262px">Lorem ipsum dolor sit amet, consectetuer adipiscing elit, sed diam nonummy nibh euismod tincidunt ut laoreet dolore magna aliquam erat volutpat. Ut wisi enim ad minim veniam, quis nostrud exerci tation ullamcorper suscipit lobortis nisl ut aliquip ex ea commodo consequat. Duis autem vel eum iriure dolor in hendrerit in vulputate velit esse molestie consequat.</p>
  <div class="box fill-navy" style="left:21.5px;top:72px"><div class="icon-badge fill-green" style="color:#fff"><svg><use href="#person"/></svg></div><h4>Heading</h4><p class="tiny" style="margin-top:3px">Lorem ipsum dolor sit amet, consectetuer adipiscing elit, sed diam nonummy nibh euismod tincidunt ut laoreet dolore magna aliquam erat volutpat. Ut wisi enim ad minim veniam, quis nostrud exerci tation</p></div>
  <div class="box fill-green" style="left:84px;top:72px"><div class="icon-badge fill-navy" style="color:#fff"><svg><use href="#person"/></svg></div><h4>Heading</h4><p class="tiny" style="margin-top:3px">Lorem ipsum dolor sit amet, consectetuer adipiscing elit, sed diam nonummy nibh euismod tincidunt ut laoreet dolore magna aliquam erat volutpat. Ut wisi enim ad minim veniam, quis nostrud exerci tation</p></div>
  <div class="box fill-navy" style="left:146.5px;top:72px"><div class="icon-badge fill-green" style="color:#fff"><svg><use href="#person"/></svg></div><h4>Heading</h4><p class="tiny" style="margin-top:3px">Lorem ipsum dolor sit amet, consectetuer adipiscing elit, sed diam nonummy nibh euismod tincidunt ut laoreet dolore magna aliquam erat volutpat. Ut wisi enim ad minim veniam, quis nostrud exerci tation</p></div>
  <div class="box fill-green" style="left:209px;top:72px"><div class="icon-badge fill-navy" style="color:#fff"><svg><use href="#person"/></svg></div><h4>Heading</h4><p class="tiny" style="margin-top:3px">Lorem ipsum dolor sit amet, consectetuer adipiscing elit, sed diam nonummy nibh euismod tincidunt ut laoreet dolore magna aliquam erat volutpat. Ut wisi enim ad minim veniam, quis nostrud exerci tation</p></div>
  <div class="foot-bar"></div><div class="page-pill">PAGE - 01</div>
</section>

<!-- Thank you -->
<section class="slide" style="left:232px;top:927px">
  <div class="logo large" style="top:8px"><span class="dot"></span>Verdano</div>
  <div class="photo" role="img" aria-label="Green-toned photo of glass office towers" style="left:0;top:32.5px;width:287px;height:122px;background:linear-gradient(135deg,#7fcc55,#3f8a2b 55%,#5cab3c)"></div>
  <div class="abs" style="right:14px;top:38px;text-align:right;color:#fff;font-weight:800;font-size:27px;line-height:25px">THANK<br>YOU!</div>
  <div class="abs" style="right:14px;top:122px;text-align:right;color:#fff;font-weight:600;font-size:12px;line-height:13px">PRESENTATION<br>TITLE GOES HERE</div>
</section>

</body>
</html>
```